Marlowe Consulting Cover 2 - Bright Ledger

Marlowe Consulting is a business consulting firm. We will publish a series of four thought leadership pieces online and via PDF. The second of the series is attached to this project. We need an eye-catching cover page with a back page that keeps with our branding. The document attached is in the final draft, and the cover and pack pages are placeholders only. You can find more about our branding and style on our website www.marloweconsulting.com.au. The other three projects can be found here with a similar brief, and you are welcome to submit a design for all 4.

```html
<!DOCTYPE html>
<html lang="en">
<head>
<meta charset="utf-8">
<title>Marlowe Consulting – Bright Ledger cover and back page</title>
<link rel="stylesheet" href="https://fonts.googleapis.com/css2?family=Poppins:wght@400;500;700&display=swap">
<style>
  :root {
    --paper: #ffffff;
    --ink: #000000;
    --white: #ffffff;
    --orange: #f7941d;
    --blue: #29abe2;
    --line-grey: #2a2a2a;
    --photo-deep: #12182a;
    --photo-mid: #3a3f4c;
    --photo-warm: #6b4a22;
  }
  * { box-sizing: border-box; margin: 0; padding: 0; }
  html, body {
    width: 1200px; height: 1200px; overflow: hidden;
    background: var(--paper);
    font-family: "Poppins", sans-serif;
    color: var(--white);
  }
  .spread { position: relative; width: 1200px; height: 1200px; }
  .page {
    position: absolute; top: 289px;
    width: 472px; height: 668px;
    background: var(--ink); overflow: hidden;
  }
  .page--back { left: 118px; }
  .page--front { left: 617px; }

  .brand {
    position: absolute; display: flex; align-items: center; gap: 6px;
    font-weight: 700; color: var(--orange); line-height: 1;
  }
  .brand__dot { border-radius: 50%; background: var(--blue); flex: none; }

  /* back page */
  .back-pattern {
    position: absolute; left: 0; top: 0; width: 472px; height: 450px;
    background: radial-gradient(ellipse at 60% 40%, #262626 0%, #141414 45%, #000 80%);
  }
  .page--back .brand { left: 71px; top: 457px; font-size: 12px; }
  .page--back .brand__dot { width: 14px; height: 14px; }
  .back-cta {
    position: absolute; left: 69px; top: 502px; width: 320px;
    font-size: 10.4px; font-weight: 500; line-height: 1.2;
  }
  .contact { position: absolute; top: 549px; font-size: 8.4px; line-height: 1.25; }
  .contact--first { left: 72px; }
  .contact--second { left: 254px; }
  .contact__name { font-weight: 700; }
  .contact__role { margin-bottom: 4px; }
  .contact__row { display: flex; align-items: center; gap: 4px; margin-top: 3px; }
  .contact__row svg { width: 10px; height: 10px; flex: none; }
  .back-bar {
    position: absolute; left: 58px; top: 616px; width: 356px; height: 23px;
    border: 1.2px solid var(--blue);
    display: flex; align-items: center; justify-content: space-between;
    padding: 0 10px; font-size: 9.6px;
  }
  .back-bar__follow { display: flex; align-items: center; gap: 8px; }
  .social-mark { width: 8px; height: 8px; background: var(--white); }

  /* front page */
  .front-photo {
    position: absolute; left: 0; top: 0; width: 472px; height: 441px;
    background:
      radial-gradient(ellipse at 78% 70%, var(--photo-warm) 0%, transparent 45%),
      linear-gradient(100deg, var(--photo-deep) 0%, var(--photo-mid) 55%, #1c2030 100%);
  }
  .page--front .brand { left: 38px; top: 52px; font-size: 19px; }
  .page--front .brand__dot { width: 22px; height: 22px; }
  .front-title {
    position: absolute; left: 38px; top: 432px;
    font-size: 32px; line-height: 37.5px; font-weight: 500; letter-spacing: 0.2px;
  }
  .front-title__lead { font-weight: 700; }
  .front-subtitle {
    position: absolute; left: 39px; top: 563px;
    font-size: 12.5px; color: var(--orange);
  }
  .front-footer {
    position: absolute; left: 38px; top: 621px; font-size: 11.5px;
  }
  .front-rule {
    position: absolute; left: 197px; right: 0; top: 631px;
    height: 1px; background: var(--orange);
  }
</style>
</head>
<body>
<main class="spread">

  <section class="page page--back" aria-label="Back page">
    <div class="back-pattern" role="img" aria-label="Faint grey decorative pattern of nested line diamonds"></div>
    <div class="brand"><span class="brand__dot"></span>Marlowe Consulting</div>
    <p class="back-cta">Contact us to find out how Marlowe Consulting can help build your company into a market leader today.</p>

    <div class="contact contact--first">
      <div class="contact__name">Hugo Marlowe</div>
      <div class="contact__role">Managing Director</div>
      <div class="contact__row">
        <svg viewBox="0 0 10 10"><circle cx="5" cy="5" r="4.3" fill="none" stroke="#fff" stroke-width="0.8"/><path d="M3.4 3c.2 1.8 1.6 3.3 3.4 3.6l.4-.9-1-.5-.5.4c-.6-.3-1-.8-1.3-1.4l.4-.5-.5-1z" fill="#fff"/></svg>
        +61 400 555 018
      </div>
      <div class="contact__row">
        <svg viewBox="0 0 10 10"><circle cx="5" cy="5" r="4.3" fill="none" stroke="#fff" stroke-width="0.8"/><rect x="2.8" y="3.5" width="4.4" height="3" rx="0.4" fill="#fff"/></svg>
        hugo@marloweconsulting.com.au
      </div>
    </div>

    <div class="contact contact--second">
      <div class="contact__name">Rupert Marlowe</div>
      <div class="contact__role">Managing Director</div>
      <div class="contact__row">
        <svg viewBox="0 0 10 10"><circle cx="5" cy="5" r="4.3" fill="none" stroke="#fff" stroke-width="0.8"/><path d="M3.4 3c.2 1.8 1.6 3.3 3.4 3.6l.4-.9-1-.5-.5.4c-.6-.3-1-.8-1.3-1.4l.4-.5-.5-1z" fill="#fff"/></svg>
        +61 400 555 027
      </div>
      <div class="contact__row">
        <svg viewBox="0 0 10 10"><circle cx="5" cy="5" r="4.3" fill="none" stroke="#fff" stroke-width="0.8"/><rect x="2.8" y="3.5" width="4.4" height="3" rx="0.4" fill="#fff"/></svg>
        rupert@marloweconsulting.com.au
      </div>
    </div>

    <div class="back-bar">
      <span>marloweconsulting.com.au</span>
      <span class="back-bar__follow">Follow us <span class="social-mark"></span><span class="social-mark"></span></span>
    </div>
  </section>

  <section class="page page--front" aria-label="Cover page">
    <div class="front-photo" role="img" aria-label="Photograph looking up at dark glass office towers with warm amber reflections"></div>
    <div class="brand"><span class="brand__dot"></span>Marlowe Consulting</div>
    <h1 class="front-title">
      <span class="front-title__lead">Bright Ledger:</span><br>
      Partnering with funds<br>
      to scale your business.
    </h1>
    <p class="front-subtitle">Bridging valuation gaps in fund raising</p>
    <p class="front-footer">marloweconsulting.com.au</p>
    <div class="front-rule"></div>
  </section>

</main>
</body>
</html>
```